Label Design for Sacha Inchi Oil in 250ml Bottle

We need unique labeling design for our product, Sacha Inchi Oil in 250ml glass bottle form. The final design should have the Company logo and the product label KAVU'S displayed. We have attached the artwork of our Company logo and the nutrients/consumption details of the product for your necessary designing. Label size for the 250ml bottle will be 122mm x 34mm.

It Company

```html
<!DOCTYPE html>
<html lang="en">
<head>
<meta charset="UTF-8">
<title>KAVU'S Sacha Inchi Oil – 250ml Labels</title>
<link href="https://fonts.googleapis.com/css2?family=Crimson+Pro:ital,wght@0,600;0,700;1,600&family=Cinzel:wght@700&family=Roboto+Condensed:wght@400;700&family=Roboto:wght@400&display=swap" rel="stylesheet">
<style>
  :root {
    --bg: #f4f4f2;
    --cream: #f8f3d9;
    --green: #1b6b3c;
    --green-dark: #155a31;
    --brown: #3b2a1f;
    --ink: #2a2a22;
    --white: #ffffff;
  }
  * { box-sizing: border-box; margin: 0; padding: 0; }
  html, body { width: 1200px; height: 960px; overflow: hidden; background: var(--bg); }
  .canvas {
    width: 1200px; height: 960px;
    display: flex; justify-content: center; align-items: center; gap: 120px;
  }

  /* ---------- Front label ---------- */
  .front-label {
    position: relative;
    width: 250px; height: 840px;
    background: var(--cream);
    border-radius: 125px 125px 10px 10px;
    overflow: hidden;
    text-align: center;
  }
  .brand-mark {
    width: 96px; height: 96px;
    margin: 52px auto 0;
    border: 3px solid var(--brown);
    border-radius: 50%;
  }
  .brand-name {
    margin-top: 130px;
    font-family: "Crimson Pro", serif;
    font-weight: 700;
    font-size: 62px;
    letter-spacing: 1px;
    color: var(--brown);
    line-height: 1;
  }
  .product-lines {
    margin-top: 26px;
    font-family: "Crimson Pro", serif;
    font-style: italic;
    font-weight: 600;
    font-size: 23px;
    line-height: 31px;
    color: var(--green);
  }
  .volume-tab {
    position: absolute; left: 50%; top: 583px;
    transform: translateX(-50%);
    width: 116px; height: 40px;
    background: var(--green);
    border-radius: 12px 12px 0 0;
    font-family: "Roboto", sans-serif;
    font-size: 22px; line-height: 42px;
    color: var(--white);
  }
  .purity-band {
    position: absolute; left: 0; right: 0; bottom: 0;
    height: 218px;
    background: var(--green);
    border-top-left-radius: 14px; border-top-right-radius: 14px;
    color: var(--white);
    padding-top: 76px;
  }
  .purity-percent {
    font-family: "Cinzel", serif; font-weight: 700;
    font-size: 36px; line-height: 1;
  }
  .purity-text {
    margin-top: 12px;
    font-family: "Crimson Pro", serif; font-weight: 600;
    font-size: 27px; letter-spacing: 0.5px;
  }

  /* ---------- Back label ---------- */
  .back-label {
    position: relative;
    width: 250px; height: 840px;
    background: var(--cream);
    border-radius: 16px;
    overflow: hidden;
    padding: 10px 8px 0;
    font-family: "Roboto Condensed", sans-serif;
    color: var(--ink);
  }
  .back-title {
    text-align: center;
    font-family: "Crimson Pro", serif; font-weight: 700;
    font-size: 27px; line-height: 30px;
    color: var(--brown);
  }
  .back-subtitle {
    margin: 4px auto 0;
    width: 218px; height: 28px;
    background: var(--green);
    border-radius: 14px;
    text-align: center;
    font-family: "Crimson Pro", serif; font-weight: 600;
    font-size: 18px; line-height: 28px;
    color: var(--white);
  }
  .nutrition-panel {
    margin-top: 7px;
    border: 2px solid var(--green);
    border-radius: 8px;
    padding: 4px 5px 5px;
    font-size: 10px; line-height: 11px;
  }
  .nutrition-heading {
    text-align: center;
    font-weight: 700; font-size: 13.5px; line-height: 14px;
    color: var(--ink);
    border-bottom: 2px solid var(--ink);
    padding-bottom: 3px;
  }
  .serving-info { padding: 4px 0 5px; border-bottom: 1px solid var(--ink); }
  .column-heads {
    display: grid; grid-template-columns: 1fr 1fr;
    text-align: center; font-weight: 700; color: var(--green);
    padding: 4px 0 3px;
    border-bottom: 3px solid var(--ink);
  }
  .nutrient { padding: 2px 0 1px; border-bottom: 1px solid var(--green); }
  .nutrient:last-child { border-bottom: none; }
  .nutrient-name { font-weight: 700; color: var(--green); }
  .nutrient-note { color: var(--green); }
  .nutrient-values {
    display: grid; grid-template-columns: 1fr 1fr;
    text-align: center;
  }
  .usage-section { padding: 6px 2px 0; font-size: 10px; line-height: 11px; }
  .usage-heading { font-weight: 700; color: var(--green); margin-bottom: 2px; }
  .usage-section + .usage-section { margin-top: 5px; }

  .maker-band {
    position: absolute; left: 0; right: 0; bottom: 0;
    height: 132px;
    background: var(--green);
    border-radius: 12px 12px 0 0;
    text-align: center; color: var(--white);
    font-size: 11.5px; line-height: 13px;
    padding-top: 40px;
  }
  .maker-tab {
    position: absolute; left: 50%; top: -22px;
    transform: translateX(-50%);
    width: 150px; height: 50px;
    background: var(--green-dark);
    border-radius: 12px 12px 0 0;
    font-weight: 700; font-size: 11.5px; line-height: 13px;
    padding-top: 6px;
  }
</style>
</head>
<body>
<main class="canvas">

  <section class="front-label" aria-label="Front label">
    <div class="brand-mark"></div>
    <h1 class="brand-name">KAVU'S</h1>
    <p class="product-lines">
      Cold Pressed<br>
      Sacha Inchi Oil<br>
      Minyak Sacha Inchi<br>
      Perahan Sejuk
    </p>
    <div class="volume-tab">250ml</div>
    <div class="purity-band">
      <div class="purity-percent">100%</div>
      <div class="purity-text">PURE ASLI</div>
    </div>
  </section>

  <section class="back-label" aria-label="Back label">
    <h2 class="back-title">Sacha Inchi Oil</h2>
    <div class="back-subtitle">Minyak Sacha Inchi</div>

    <div class="nutrition-panel">
      <div class="nutrition-heading">Maklumat Pemakanan/<br>Nutrition Information</div>
      <div class="serving-info">
        Saiz Hidangan/Serving Size:<br>
        1 sudu Camca /1 tablespoon (15ml)<br>
        Hidangan Setiap Botol/Serving<br>
        Per Bottle: 16
      </div>
      <div class="column-heads">
        <span>Setiap/<br>Per 100ml</span>
        <span>Setiap Hidangan/<br>Per Serving 15ml</span>
      </div>

      <div class="nutrient">
        <div class="nutrient-name">Tenaga / Energy</div>
        <div class="nutrient-values"><span>806 kcal (3386 kJ)</span><span>121 kCal (508 kJ)</span></div>
        <div class="nutrient-name">Protein / Protein</div>
        <div class="nutrient-values"><span>0g</span><span>0g</span></div>
      </div>
      <div class="nutrient">
        <div class="nutrient-name">Karbohidrat / Carbohydrate</div>
        <div class="nutrient-values"><span>18.3g</span><span>2.7g</span></div>
      </div>
      <div class="nutrient">
        <div class="nutrient-name">Lemak / Fat</div>
        <div class="nutrient-note">yang terdiri daripada / comprising of</div>
        <div class="nutrient-values"><span>81.4g</span><span>12.2g</span></div>
      </div>
      <div class="nutrient">
        <div class="nutrient-name">Asid Lemak Monotidaktepu /<br>Monounsaturated Fatty Acid</div>
        <div class="nutrient-values"><span>4.6g</span><span>0.7g</span></div>
      </div>
      <div class="nutrient">
        <div class="nutrient-name">Omega-9</div>
        <div class="nutrient-values"><span>4.4g</span><span>0.7g</span></div>
      </div>
      <div class="nutrient">
        <div class="nutrient-name">Asid Lemak Politidaktepu/<br>Polyunsaturated Fatty Acid</div>
        <div class="nutrient-values"><span>71.7g</span><span>10.8</span></div>
      </div>
      <div class="nutrient">
        <div class="nutrient-name">Omega-3</div>
        <div class="nutrient-values"><span>44.1g</span><span>6.6g</span></div>
      </div>
      <div class="nutrient">
        <div class="nutrient-name">Omega-6</div>
        <div class="nutrient-values"><span>27.5g</span><span>4.1g</span></div>
      </div>
      <div class="nutrient">
        <div class="nutrient-name">Asid Lemak Tepu/<br>Saturated Fatty Acid</div>
        <div class="nutrient-values"><span>5.1g</span><span>0.8g</span></div>
      </div>
      <div class="nutrient">
        <div class="nutrient-name">Asid Trans Lemak / Trans Fatty Acid</div>
        <div class="nutrient-values"><span>0.1g</span><span>0g</span></div>
      </div>
      <div class="nutrient">
        <div class="nutrient-name">Kolesterol / Cholesterol</div>
        <div class="nutrient-values"><span>0g</span><span>0g</span></div>
      </div>
    </div>

    <div class="usage-section">
      <div class="usage-heading">Arahan Penggunaan / Directions For Use</div>
      Campurkan 1 sudu camca minyak ke dalam salad dan gaul bersama./ Mix 1 tablespoon of oil into salad &amp; mix well together.
    </div>
    <div class="usage-section">
      <div class="usage-heading">Penyimpanan / Storage</div>
      Simpan di tempat yang dingin, kering dan jauhi daripada haba dan sinaran cahaya matahari. / Store in a cold and dry place away from heat and direct sunlight.
    </div>

    <div class="maker-band">
      <div class="maker-tab">Owner of the Rights<br>of Manufacture</div>
      Inchi Harvest Trading Pte. Ltd.<br>
      Company Reg#. 201845117K<br>
      8 Meranti Lane<br>
      #03-21 Meranti Court<br>
      Singapore 188410
    </div>
  </section>

</main>
</body>
</html>
```